Startup company business card (Media & Advertising)

we need a business card design for a company that is a startup in the media and aggregation industry. Card needs to look funky and of a new breed/modern and upmarket.

Target Market(s)

advertisers/ brand agencies & media publishers

Industry/Entity Type

Advertising

Contact Information for Business Card

Please ensure the front face signifies our brand (plumvexo.com) and back has details for the contact. Standard contact such as phone , address, email , website etc.

Font styles to use
Other font styles liked:
• use styleguide and logo font and color

Colors

Designer to choose colors to be used in the design.

Requirements
Must have
• We are disrupting the media and agency industry so subtlety would be good to use imagery to signify this
Nice to have
• Please use logo colors for branding
Should not have
• be as creative and provide few options. Pick a brand color from logo and styleguide

```html
<!DOCTYPE html>
<html lang="en">
<head>
<meta charset="utf-8">
<title>plumvexo business card</title>
<link rel="stylesheet" href="https://fonts.googleapis.com/css2?family=Arvo:wght@400;700&family=Nunito+Sans:wght@400;600&display=swap">
<style>
  :root {
    --stage: #1d1d20;
    --ink: #0a0a0c;
    --paper: #ffffff;
    --brand-red: #e8364a;
    --brand-wine: #9b1840;
    --text-dark: #1b1b1f;
    --text-mid: #3a3a40;
    --white: #ffffff;
  }
  * { box-sizing: border-box; margin: 0; padding: 0; }
  html, body {
    width: 1200px; height: 900px; overflow: hidden;
    background: var(--stage);
  }
  .stage {
    width: 1200px; height: 900px;
    display: flex; flex-direction: column; align-items: center; justify-content: center;
    gap: 60px;
  }
  .card {
    position: relative;
    width: 630px; height: 360px;
    overflow: hidden;
    box-shadow: 0 10px 30px rgba(0,0,0,.45);
  }
  .brand {
    display: flex; align-items: center; gap: 16px;
    font-family: "Arvo", serif; font-weight: 700;
    color: var(--white); font-size: 40px; letter-spacing: 1px;
  }
  .brand-dot {
    width: 46px; height: 46px; border-radius: 50%;
    background: var(--brand-red);
  }

  /* Front */
  .card-front { background: var(--ink); }
  .card-front .brand {
    position: absolute; left: 0; right: 0; top: 110px; justify-content: center;
  }
  .tagline-band {
    position: absolute; left: 0; right: 0; bottom: 0; height: 88px;
    background: linear-gradient(90deg, var(--brand-red) 0%, var(--brand-wine) 100%);
    display: flex; flex-direction: column; justify-content: center; align-items: center;
    font-family: "Arvo", serif; font-size: 14px; letter-spacing: 2.4px;
    color: var(--white); text-transform: uppercase; line-height: 1.35;
  }

  /* Back */
  .card-back { background: var(--paper); }
  .back-header {
    position: absolute; left: 0; right: 0; top: 0; height: 200px;
    background: var(--ink);
    display: flex; justify-content: center; align-items: center;
    padding-bottom: 12px;
  }
  .header-rule {
    position: absolute; left: 60px; right: 60px; bottom: 8px; height: 1px;
    background: var(--brand-red);
  }
  .contact-block {
    position: absolute; left: 0; right: 0; top: 226px;
    display: flex; justify-content: center; align-items: flex-start; gap: 16px;
  }
  .person { text-align: right; }
  .person-name {
    font-family: "Arvo", serif; font-size: 30px; color: var(--text-dark); line-height: 1.05;
  }
  .person-role {
    font-family: "Nunito Sans", sans-serif; font-size: 17px; color: var(--text-mid);
  }
  .divider { width: 1px; height: 72px; background: var(--brand-red); }
  .contact-list { list-style: none; font-family: "Nunito Sans", sans-serif; font-size: 17px; color: var(--text-dark); }
  .contact-list li { display: flex; align-items: center; gap: 10px; line-height: 24px; }
  .contact-list svg { width: 16px; height: 16px; flex: none; }
  .address {
    position: absolute; left: 0; right: 0; top: 312px; text-align: center;
    font-family: "Nunito Sans", sans-serif; font-size: 18px; color: var(--text-dark);
  }
</style>
</head>
<body>
<main class="stage">
  <section class="card card-front">
    <div class="brand"><span class="brand-dot"></span><span>plumvexo</span></div>
    <div class="tagline-band">
      <span>We are disrupting the media and agency industry</span>
      <span>so subtlety would be good to use imagery to signify this</span>
    </div>
  </section>

  <section class="card card-back">
    <header class="back-header">
      <div class="brand"><span class="brand-dot"></span><span>plumvexo</span></div>
      <div class="header-rule"></div>
    </header>
    <div class="contact-block">
      <div class="person">
        <p class="person-name">Dario Mensel</p>
        <p class="person-role">CEO &amp; Founder</p>
      </div>
      <div class="divider"></div>
      <ul class="contact-list">
        <li>
          <svg viewBox="0 0 16 16" fill="none" stroke="#e8364a" stroke-width="1.4"><path d="M4 2l2.5 3-1.5 1.5c.8 1.8 2.2 3.2 4 4L10.5 9 13.5 11.5 12 14C7 13.5 2.5 9 2 4z"/></svg>
          <span>+34 611.502.938</span>
        </li>
        <li>
          <svg viewBox="0 0 16 16" fill="none" stroke="#e8364a" stroke-width="1.4"><rect x="1.5" y="3.5" width="13" height="9"/><path d="M1.5 3.5L8 9l6.5-5.5"/></svg>
          <span>mensel@plumvexo.com</span>
        </li>
        <li>
          <svg viewBox="0 0 16 16" fill="none" stroke="#e8364a" stroke-width="1.4"><circle cx="8" cy="8" r="6.5"/><ellipse cx="8" cy="8" rx="2.8" ry="6.5"/><path d="M1.5 8h13"/></svg>
          <span>www.plumvexo.com</span>
        </li>
      </ul>
    </div>
    <p class="address">P.O. Box 4180 Harlow, Wyoming 83010</p>
  </section>
</main>
</body>
</html>
```